Ridgeway Patrol Website Design

Hello Designers. I am an agency and am helping a security company get a better look. I have a new logo and a car done up. We are looking for a fresh look using the blue and the gold. Open to a complimentary color.

Here is the old site
https://moravanguard.com/

Here is another design for photos and everything. We weren't sold on it because we wanted to make it simple like the first one.

https://ww2.moravanguard.com/

Attached is also the copy I would like to put on there.

I am looking for tough, competent and simple. Our customers are contruction companies, event planners etc. It has to be clean and easy.

One thing we can't provide yet is photos. We are anticipating photos of our team with arms folded beside the car, close up of the owner with a logo'd shirt on. Pictures of an Ridgeway Patrol job site etc. (which most of the time is construction. They also do Mall security. You can see if you want to use stock photos for now.

I wanted to get the look of the front page done first. Hoping for something really awesome. Have fun.

```html
<!DOCTYPE html>
<html lang="en">
<head>
<meta charset="utf-8">
<title>Ridgeway Patrol – Security Services</title>
<link href="https://fonts.googleapis.com/css2?family=Lexend:wght@300;400&family=Open+Sans:wght@400;600;700&display=swap" rel="stylesheet">
<style>
:root{
  --navy:#14233f;
  --navy-deep:#0f1b33;
  --gold:#a9843a;
  --gold-light:#c09a4c;
  --ink:#1b1b1b;
  --text:#5f5f5f;
  --white:#ffffff;
  --panel:#f7f7f7;
  --line:#d9d9d9;
}
*{box-sizing:border-box;margin:0;padding:0}
html,body{width:1200px;height:3989px;overflow:hidden}
body{font-family:"Open Sans",Arial,sans-serif;color:var(--ink);background:var(--white);position:relative}
section,header,footer,nav{position:relative;width:1200px;display:block}
.abs{position:absolute}
.heading{font-family:"Lexend",Arial,sans-serif;font-weight:400;letter-spacing:3px}
.tag{position:absolute;background:var(--gold);color:var(--white);font-size:12px;font-weight:700;display:flex;align-items:center;justify-content:center;letter-spacing:.3px;white-space:nowrap}
.btn{position:absolute;display:flex;align-items:center;justify-content:center;color:var(--white);font-weight:700;font-size:20px;white-space:nowrap}
.btn-navy{background:var(--navy)}
.btn-gold{background:var(--gold)}
.placeholder{position:absolute}

/* top bar */
.topbar{height:60px;background:var(--navy)}
.topbar p{position:absolute;top:18px;color:var(--white);font-size:15px;font-weight:600;white-space:nowrap}
.topbar .phone-box{position:absolute;left:697px;top:18px;width:26px;height:24px;border:1.5px solid var(--white);display:flex;align-items:center;justify-content:center}

/* nav */
.nav{height:73px;background:var(--white)}
.brand{position:absolute;left:116px;top:18px;display:flex;align-items:center;gap:10px}
.brand .mark{width:34px;height:34px;background:var(--navy)}
.brand span{font-size:20px;font-weight:700;color:var(--navy);letter-spacing:.5px;white-space:nowrap}
.nav a{position:absolute;top:24px;font-size:16px;color:var(--ink);text-decoration:none;white-space:nowrap}
.nav a.active{color:var(--gold);font-weight:600}
.login{position:absolute;left:978px;top:18px;width:110px;height:37px;background:var(--navy);color:var(--white);font-size:16px;font-weight:600;display:flex;align-items:center;justify-content:center}

/* hero */
.hero{height:579px;background:linear-gradient(90deg,#1a1a1a 0%,#242424 50%,#1c1c1c 100%)}
.hero .photo{left:0;top:0;width:640px;height:579px;background:radial-gradient(ellipse at 45% 45%,#4a4a4a 0%,#2c2c2c 45%,#1a1a1a 80%)}
.hero .kicker{left:626px;top:106px;color:var(--white);font-size:20px;font-weight:600}
.hero h1{left:625px;top:142px;color:var(--white);font-size:40px;line-height:52px;font-weight:400}
.hero p.body{left:627px;top:248px;width:468px;color:#c9c9c9;font-size:15px;line-height:26px}
.hero .btn{left:627px;top:341px;width:178px;height:50px}
.hero svg{position:absolute;left:0;bottom:0}

/* about */
.about{height:531px}
.about h2{left:111px;top:115px;font-size:38px}
.about p{left:111px;top:172px;width:488px;font-size:16px;line-height:27px;color:var(--text);text-align:justify}
.ticks{position:absolute;list-style:none}
.ticks li{display:flex;align-items:flex-start;gap:10px;font-size:16px;line-height:27px;color:var(--ink);margin-bottom:7px}
.ticks svg{flex:none;margin-top:7px}
.about .btn{left:111px;top:389px;width:178px;height:52px}
.about .frame{left:632px;top:48px;width:475px;height:420px}
.about .photo{left:647px;top:64px;width:441px;height:388px;background:linear-gradient(135deg,#c9ccd2 0%,#8d949f 40%,#2c313b 100%)}

/* services */
.services{height:669px;background:radial-gradient(ellipse at 30% 40%,#1d2f52 0%,var(--navy) 55%,var(--navy-deep) 100%)}
.services h2{top:140px;width:1200px;text-align:center;color:var(--white);font-size:40px}
.card{position:absolute;display:flex;gap:14px;padding:26px 14px 0 10px}
.card svg{flex:none}
.card h3{font-size:20px;font-weight:700;color:var(--white);letter-spacing:.5px;margin-bottom:10px;text-transform:uppercase;white-space:nowrap}
.card p{font-size:13px;line-height:21px;color:#e6e6e6;text-align:justify}
.card .more{display:block;margin-top:12px;font-size:13px;font-weight:700;color:var(--white)}
.card.featured{background:var(--white)}
.card.featured h3,.card.featured .more{color:var(--gold)}
.card.featured p{color:var(--gold-light)}

/* career */
.career{height:580px}
.career .photo{left:111px;top:87px;width:429px;height:402px;background:linear-gradient(150deg,#2b4d86 0%,#7f98bf 45%,#d8dde6 70%,#3a5a90 100%)}
.career h2{left:598px;top:140px;font-size:40px;white-space:nowrap}
.career p{left:598px;top:200px;width:489px;font-size:16px;line-height:27.5px;color:var(--text);text-align:justify}
.career .btn{left:598px;top:432px;width:178px;height:50px}

/* hiring */
.hiring{height:457px;background:radial-gradient(ellipse at 20% 40%,#20345a 0%,var(--navy) 60%,var(--navy-deep) 100%)}
.hiring h2{left:111px;top:140px;color:var(--white);font-size:26px}
.hiring p{left:111px;top:192px;width:365px;color:var(--white);font-size:15px;line-height:27px}
.hiring .btn{left:111px;top:326px;width:200px;height:51px}
.hiring .photo{left:492px;top:8px;width:708px;height:433px;background:radial-gradient(ellipse at 50% 60%,#e7e8eb 0%,#b9bec7 35%,rgba(20,35,63,0) 70%)}

/* contact */
.contact{height:526px}
.contact h2{left:111px;top:154px;font-size:34px}
.contact .lead{left:111px;top:217px;width:380px;font-size:15px;line-height:30px;color:var(--text)}
.contact h4{position:absolute;left:111px;top:308px;font-size:20px;font-weight:700;white-space:nowrap}
.social{position:absolute;top:368px;width:40px;height:39px;background:var(--navy);display:flex;align-items:center;justify-content:center}
.social i{display:block;width:12px;height:12px;border:2px solid var(--white);border-radius:50%}
.form{position:absolute;left:559px;top:87px;width:529px;height:398px;background:var(--panel);border:1px solid #ececec}
.form h3{position:absolute;top:33px;width:100%;text-align:center;font-size:24px}
.field{position:absolute;background:var(--white);border:1.5px solid var(--line);font-family:Georgia,serif;font-size:14px;color:#8a8a8a;padding:14px 0 0 19px}
.submit{position:absolute;left:206px;top:326px;width:131px;height:47px;background:var(--gold);color:var(--white);font-weight:700;font-size:16px;display:flex;align-items:center;justify-content:center}

/* footer */
.footer{height:514px}
.footer .brand{left:116px;top:124px}
.footer .brand .mark{background:var(--white)}
.footer .brand span{color:var(--white);font-size:24px}
.footer .about-text{left:111px;top:214px;width:335px;color:#e3e3e3;font-size:15px;line-height:31px}
.footer h5{position:absolute;top:122px;color:var(--white);font-family:"Lexend",Arial,sans-serif;font-weight:400;font-size:20px;letter-spacing:1.5px;white-space:nowrap}
.links{position:absolute;list-style:none;top:170px}
.links li{display:flex;align-items:center;gap:12px;color:#e3e3e3;font-size:15px;height:48px;margin-top:-14px}
.links li::before{content:"";width:6px;height:6px;border-radius:50%;background:var(--white)}
.info{position:absolute;left:870px;display:flex;gap:14px;color:#e3e3e3;font-size:15px;line-height:21px}
.info svg{flex:none}
.footer .rule{position:absolute;left:111px;top:418px;width:980px;height:1px;background:#7a8398}
.footer .copy{position:absolute;top:451px;width:1200px;text-align:center;color:var(--white);font-size:17px}
</style>
</head>
<body>

<header class="topbar">
  <p style="left:113px">We're ready, so give us a call</p>
  <div class="phone-box">
    <svg width="14" height="14" viewBox="0 0 24 24" fill="none" stroke="#fff" stroke-width="2"><path d="M5 3h4l2 5-3 2a12 12 0 0 0 6 6l2-3 5 2v4a2 2 0 0 1-2 2A17 17 0 0 1 3 5a2 2 0 0 1 2-2z"/></svg>
  </div>
  <p style="left:737px">We're Are Available in 24/7:&nbsp; (506) 555-0147</p>
</header>

<nav class="nav">
  <div class="brand"><div class="mark"></div><span>RIDGEWAY PATROL</span></div>
  <a class="active" href="#" style="left:356px">Home</a>
  <a href="#" style="left:460px">About</a>
  <a href="#" style="left:562px">Security Service</a>
  <a href="#" style="left:746px">Career</a>
  <a href="#" style="left:856px">Training</a>
  <div class="login">Login</div>
</nav>

<section class="hero">
  <div class="placeholder photo" role="img" aria-label="Security officer in a branded jacket speaking into a radio, seen from behind"></div>
  <p class="abs kicker">New Brunswick's</p>
  <h1 class="abs heading">SECURITY<br>PROFESSIONAL</h1>
  <p class="abs body">We're looking for 10 professional part-time and full-time security officers . We want hard-working, punctual individuals that want to be part of a supportive and enriching team.</p>
  <div class="btn btn-gold">Get Started</div>
  <svg width="1200" height="70" viewBox="0 0 1200 70">
    <polygon points="0,16 697,16 766,70 0,70" fill="#fff"/>
    <polyline points="0,11 697,11 766,65 1200,65" fill="none" stroke="#a9843a" stroke-width="8"/>
  </svg>
</section>

<section class="about">
  <div class="tag" style="left:111px;top:64px;width:194px;height:38px">ABOUT RIDGEWAY PATROL</div>
  <h2 class="abs heading">What We Are</h2>
  <p class="abs">Ridgeway Patrol was founded in 2005 to meet the growing demand for event security in Greater Moncton and south Eastern New Brunswick.</p>
  <ul class="ticks" style="left:111px;top:264px">
    <li><svg width="16" height="12" viewBox="0 0 16 12" fill="none" stroke="#a9843a" stroke-width="2"><path d="M0 6h14M9 1l5 5-5 5"/></svg>Confidentely Services</li>
    <li><svg width="16" height="12" viewBox="0 0 16 12" fill="none" stroke="#a9843a" stroke-width="2"><path d="M0 6h14M9 1l5 5-5 5"/></svg>24 years of security experience</li>
    <li><svg width="16" height="12" viewBox="0 0 16 12" fill="none" stroke="#a9843a" stroke-width="2"><path d="M0 6h14M9 1l5 5-5 5"/></svg>200+ bilingual security professionals</li>
  </ul>
  <div class="btn btn-navy">Read More</div>
  <svg class="abs frame" viewBox="0 0 475 420"><polygon points="0,0 475,0 475,420 457,404 15,404 15,16" fill="#a9843a"/></svg>
  <div class="placeholder photo" role="img" aria-label="Security officer on the phone at a monitoring desk with CCTV screens"></div>
</section>

<section class="services">
  <div class="tag" style="left:531px;top:84px;width:139px;height:36px">WHAT WE OFFER</div>
  <h2 class="abs heading">Our Services</h2>

  <div class="card" style="left:111px;top:220px;width:307px;height:182px">
    <svg width="48" height="56" viewBox="0 0 48 56" fill="none" stroke="#fff" stroke-width="2"><circle cx="24" cy="30" r="22"/><rect x="15" y="28" width="18" height="14" rx="2"/><path d="M18 28v-5a6 6 0 0 1 12 0v5"/></svg>
    <div><h3>Static Security</h3><p>We provide stationary and foot patrol for retail spaces and ensure our uniformed security</p><span class="more">Read More</span></div>
  </div>
  <div class="card featured" style="left:441px;top:220px;width:328px;height:182px">
    <svg width="54" height="56" viewBox="0 0 54 56" fill="none" stroke="#a9843a" stroke-width="2"><circle cx="27" cy="28" r="24"/><rect x="17" y="12" width="20" height="8" rx="3"/><path d="M14 44c3-8 23-8 26 0"/></svg>
    <div><h3>Security Patrol</h3><p>We provide stationary and foot patrol for retail spaces and ensure our uniformed security</p><span class="more">Read More</span></div>
  </div>
  <div class="card" style="left:790px;top:220px;width:301px;height:182px">
    <svg width="54" height="56" viewBox="0 0 54 56" fill="none" stroke="#fff" stroke-width="2"><rect x="3" y="6" width="30" height="40"/><path d="M9 14h18M9 22h12M9 30h10"/><circle cx="34" cy="36" r="9"/><path d="M40 42l8 8"/></svg>
    <div><h3>Investigations</h3><p>Whatever your investigative needs are give us a call we would be glad to help.</p><span class="more">Read More</span></div>
  </div>

  <div class="card" style="left:108px;top:442px;width:310px;height:165px">
    <svg width="50" height="56" viewBox="0 0 50 56" fill="none" stroke="#fff" stroke-width="2"><rect x="3" y="24" width="34" height="28" rx="2"/><path d="M10 24v-8a10 10 0 0 1 20 0v8"/><circle cx="14" cy="36" r="4"/><path d="M22 34h10M22 42h8"/><circle cx="40" cy="46" r="8"/><path d="M36 46l3 3 5-6"/></svg>
    <div><h3>Consulting</h3><p>We will work closely with staff, event planners, emergency responders and workplace health</p><span class="more">Read More</span></div>
  </div>
  <div class="card" style="left:445px;top:442px;width:324px;height:165px">
    <svg width="58" height="56" viewBox="0 0 58 56" fill="none" stroke="#fff" stroke-width="2"><rect x="3" y="14" width="36" height="34" rx="2"/><path d="M10 26h14M10 34h10"/><path d="M44 4l10 4v10c0 7-5 11-10 13-5-2-10-6-10-13V8z" fill="#fff"/><path d="M40 17l3 3 5-6" stroke="#14233f"/></svg>
    <div><h3>Retail Security</h3><p>We provide stationary and foot patrol for retail spaces and ensure our uniformed</p><span class="more">Read More</span></div>
  </div>
  <div class="card" style="left:786px;top:442px;width:305px;height:165px">
    <svg width="58" height="56" viewBox="0 0 58 56" fill="none" stroke="#fff" stroke-width="2"><rect x="3" y="22" width="38" height="26" rx="2"/><path d="M3 30h38M9 40h10"/><path d="M42 4l10 4v10c0 7-5 11-10 13-5-2-10-6-10-13V8z"/><circle cx="42" cy="16" r="3"/></svg>
    <div><h3>VIP Security</h3><p>We work closely with our high profile clients to identify risk, and how best to</p><span class="more">Read More</span></div>
  </div>
</section>

<section class="career">
  <div class="placeholder photo" role="img" aria-label="Two uniformed security staff working together at a computer in a control room"></div>
  <div class="tag" style="left:598px;top:90px;width:112px;height:36px">OUR CAREER</div>
  <h2 class="abs heading">Professionals Wanted</h2>
  <p class="abs">Ridgeway Patrol is always looking for applicants. We welcome applicants who don't mind being on their feet for long periods of time, don't mind working outside normal business hours and enjoy.</p>
  <ul class="ticks" style="left:598px;top:321px">
    <li><svg width="18" height="18" viewBox="0 0 18 18" fill="none" stroke="#a9843a" stroke-width="2"><path d="M16 8.5A7.5 7.5 0 1 1 12 2.3"/><path d="M5 8l3.5 3.5L17 3"/></svg>Part Time Administrative &amp; Full Time Security Officers</li>
    <li><svg width="18" height="18" viewBox="0 0 18 18" fill="none" stroke="#a9843a" stroke-width="2"><path d="M16 8.5A7.5 7.5 0 1 1 12 2.3"/><path d="M5 8l3.5 3.5L17 3"/></svg><span>Full Time Security Officers &amp; Part Time Team Leads<br>for specific events.</span></li>
  </ul>
  <div class="btn btn-navy">Read More</div>
</section>

<section class="hiring">
  <div class="tag" style="left:111px;top:83px;width:81px;height:37px">HIRING</div>
  <h2 class="abs heading">Ridgeway Patrol</h2>
  <p class="abs">Our professional employees are given the tools to succeed. From crowd control to protecting people and property, our team is trained with industry best practices.</p>
  <div class="btn btn-gold">Get In Touch</div>
  <div class="placeholder photo" role="img" aria-label="White branded patrol car with a suited security guard standing beside it"></div>
</section>

<section class="contact">
  <h2 class="abs heading">Let's Talk</h2>
  <p class="abs lead">Security jobs and careers are available in an expanding, stable, and diverse field.</p>
  <h4>Stay Tuned with is on Social Networks</h4>
  <div class="social" style="left:111px" aria-label="Social network link"><i></i></div>
  <div class="social" style="left:167px" aria-label="Social network link"><i></i></div>
  <div class="social" style="left:223px" aria-label="Social network link"><i></i></div>
  <div class="social" style="left:279px" aria-label="Social network link"><i></i></div>

  <div class="form">
    <h3 class="heading" style="letter-spacing:2px">Contact us</h3>
    <div class="field" style="left:33px;top:95px;width:222px;height:47px">First Name*</div>
    <div class="field" style="left:281px;top:95px;width:222px;height:47px">Last Name*</div>
    <div class="field" style="left:33px;top:157px;width:222px;height:47px">Email*</div>
    <div class="field" style="left:281px;top:157px;width:222px;height:47px">Phone Number*</div>
    <div class="field" style="left:33px;top:217px;width:470px;height:83px">Message*</div>
    <div class="submit">SUBMIT</div>
  </div>
</section>

<footer class="footer">
  <svg class="abs" style="left:0;top:0" width="1200" height="514" viewBox="0 0 1200 514">
    <polygon points="0,0 433,0 503,51 1200,51 1200,514 0,514" fill="#14233f"/>
    <polyline points="0,2 433,2 503,53 1200,53" fill="none" stroke="#a9843a" stroke-width="7"/>
  </svg>
  <div class="brand"><div class="mark"></div><span>RIDGEWAY PATROL</span></div>
  <p class="abs about-text">We offer complete security services including event security, uniformed security and personal security services.our team is trained with industry best practices.</p>

  <h5 style="left:509px">Quick Links</h5>
  <ul class="links" style="left:509px"><li>Home</li><li>About</li><li>Service</li><li>Contact</li></ul>

  <h5 style="left:697px">Help Links</h5>
  <ul class="links" style="left:697px"><li>FAQ</li><li>Terms</li><li>Privacy</li><li>Conditions</li></ul>

  <h5 style="left:875px">Contact us</h5>
  <div class="info" style="top:176px">
    <svg width="20" height="22" viewBox="0 0 20 22" fill="none" stroke="#fff" stroke-width="1.6"><path d="M10 21s-7-7-7-12a7 7 0 0 1 14 0c0 5-7 12-7 12z"/><circle cx="10" cy="9" r="2.5"/></svg>
    <span>2240 Harbourview Rd.<br>Suite 204, Riverview NB<br>E1B 4K7</span>
  </div>
  <div class="info" style="top:264px">
    <svg width="20" height="20" viewBox="0 0 24 24" fill="none" stroke="#fff" stroke-width="1.8"><path d="M5 3h4l2 5-3 2a12 12 0 0 0 6 6l2-3 5 2v4a2 2 0 0 1-2 2A17 17 0 0 1 3 5a2 2 0 0 1 2-2z"/></svg>
    <span>506.555.0147</span>
  </div>
  <div class="info" style="top:318px">
    <svg width="20" height="16" viewBox="0 0 20 16" fill="none" stroke="#fff" stroke-width="1.6"><rect x="1" y="1" width="18" height="14"/><path d="M1 1l9 8 9-8"/></svg>
    <span>info@ridgewaypatrol.com</span>
  </div>

  <div class="rule"></div>
  <p class="copy">Copyrights@2022.All Rights Reserved</p>
</footer>

</body>
</html>
```